Church needs a street sign design

We're a small church located in Silicon Valley, California. Our website is https://www.hfbmerrow.org/ and our address is 4817 Larkfield Ave, San Jose, California, 95873. You can look up our location on Google Maps to see the sign from Street View. I have uploaded an image of the street sign as well. The marquee, the top section of the sign, and the separating line between them both will be removed. We're seeking a design for a new backlit acrylic insert that will go on the front of the light box and the back of the lightbox. The acrylic sign will fill the entire external frame. In the future, we may build a decorative wood frame around the structural legs, as visualized in one of the uploaded files. The church's brand colors are: #003366 (dark blue), #ff6600 (vibrant orange), #228b22 (forest green). I have also uploaded the church's logo assets. Our primary font is Montserrat and the secondary is Poppins. You can deviate from these colors/fonts if the sign is still coherent with the rest of our branding. Our branding values are mission, truth, passion, and community (please do not put those words on the sign! They are just intended to guide the look of the design). The sign dimensions are 96" by 47.5". Keep in mind that the sign will be backlit on a busy street side. It will also be positioned next to an old-looking church building. We do NOT want a sign that looks traditional, old, or antiquated. Instead, we want a modern-looking sign that pairs well with our old building while helping it look more modern too. We would also like the web address clearly visible on the sign: hfbmerrow.org. If you have any questions, just let me know!

```html
<!DOCTYPE html>
<html lang="en">
<head>
<meta charset="utf-8">
<title>Hillford Bible Church – Street Sign Insert</title>
<link rel="stylesheet" href="https://fonts.googleapis.com/css2?family=Montserrat:wght@600;700;800&family=Poppins:wght@600;700;800&display=swap">
<style>
  :root {
    --page-bg: #b3b9c5;
    --sky-deep: #1aa6f0;
    --sky-mid: #3cc4f5;
    --sky-light: #bff0fb;
    --band-orange: #ff5a00;
    --band-red: #ff1a00;
    --ink: #050505;
    --brand-blue: #003366;
    --white: #ffffff;
  }
  * { box-sizing: border-box; margin: 0; padding: 0; }
  html, body { width: 762px; height: 1200px; overflow: hidden; }
  body { background: var(--page-bg); position: relative; }

  .sign {
    position: absolute;
    left: 31px;
    top: 427px;
    width: 700px;
    height: 346px;
    overflow: hidden;
    box-shadow: 0 10px 14px rgba(0,0,0,0.35);
  }
  .sign__sky {
    position: absolute; inset: 0;
    background:
      radial-gradient(ellipse at 75% 20%, rgba(255,255,255,0.55), transparent 45%),
      radial-gradient(ellipse at 10% 75%, rgba(255,255,255,0.5), transparent 40%),
      linear-gradient(180deg, var(--sky-deep) 0%, var(--sky-mid) 55%, var(--sky-light) 100%);
  }

  .church-name {
    position: absolute;
    left: 34px;
    top: 22px;
    display: flex;
    align-items: center;
    gap: 18px;
  }
  .church-name__mark {
    width: 26px; height: 26px;
    background: var(--brand-blue);
  }
  .church-name__text {
    font-family: "Montserrat", sans-serif;
    font-weight: 800;
    color: var(--ink);
    line-height: 0.95;
  }
  .church-name__main { display: block; font-size: 84px; letter-spacing: -1px; }
  .church-name__sub { display: block; font-size: 33px; letter-spacing: 0.5px; margin-top: 4px; }

  .info-band {
    position: absolute;
    left: 34px;
    right: 0;
    top: 169px;
    height: 149px;
    border-radius: 14px 0 0 14px;
    background: linear-gradient(100deg, var(--band-orange) 0%, #ff4d00 45%, var(--band-red) 80%, #ff3a00 100%);
  }
  .location {
    position: absolute;
    left: 40px;
    top: 22px;
    display: flex;
    align-items: flex-start;
    gap: 8px;
  }
  .location__pin { width: 26px; height: 40px; margin-top: 2px; }
  .location__region {
    font-family: "Montserrat", sans-serif;
    font-weight: 800;
    font-size: 27px;
    color: var(--white);
    line-height: 1;
  }
  .location__street {
    font-family: "Poppins", sans-serif;
    font-weight: 700;
    font-size: 15.5px;
    color: var(--white);
    line-height: 1.2;
    margin-top: 5px;
  }
  .web-address {
    position: absolute;
    left: 40px;
    top: 78px;
    font-family: "Poppins", sans-serif;
    font-weight: 800;
    font-size: 50px;
    color: var(--white);
    letter-spacing: -0.5px;
    line-height: 1;
  }
</style>
</head>
<body>
  <main class="sign">
    <div class="sign__sky" role="img" aria-label="Bright blue sky with soft white clouds and light rays"></div>

    <h1 class="church-name">
      <span class="church-name__mark" aria-hidden="true"></span>
      <span class="church-name__text">
        <span class="church-name__main">HILLFORD</span>
        <span class="church-name__sub">BIBLE CHURCH</span>
      </span>
    </h1>

    <section class="info-band" role="img" aria-label="Orange and red cloud texture band" >
      <div class="location">
        <svg class="location__pin" viewBox="0 0 26 40" aria-hidden="true">
          <path d="M13 0C5.8 0 0 5.6 0 12.6 0 21 13 40 13 40S26 21 26 12.6C26 5.6 20.2 0 13 0z" fill="var(--brand-blue)"/>
          <circle cx="13" cy="12.5" r="6" fill="var(--band-orange)"/>
        </svg>
        <div>
          <p class="location__region">SILICON VALLEY, CALIFORNIA</p>
          <p class="location__street">4817 Larkfield Ave, San Jose, California, 95873</p>
        </div>
      </div>
      <p class="web-address">www.hfbmerrow.org</p>
    </section>
  </main>
</body>
</html>
```